Book Cover for Memoir: Sexual Assault and Traumatic Stress

I need a cover design for a memoir that is a victim's story of a sexual assault. I will need a print-on-demand cover, an eBook cover, and a 3D thumbnail image. The thumbnail and eBook cover will be used immediately, and the POD cover will be used in a few months with the full manuscript is ready. Therefore, I need an artist who is willing to make small adjustments if needed once the page count is set.

I have a image I have purchased that should give you an idea of the desired direction, but you can feel free to use your own images. I have attached some examples of book covers I like. I attached a color palette for fonts.

Overall Look: Fonts should be feminine and thin, but large to stand out. Look should be simple and elegant, and display and overall depressing feeling. There should be enough detail though to make it look professionally put together. Not TOO minimalistic.

I have also attached the Print Harbor templates if you choose to use those. If not, ensure there is an open place for the barcode on the bottom right.

Requirements
Must have
• Title: Beneath Quiet Rain
Subtitle: One Woman's Account of Fear, Guilt & Silence
Author: Dana Ruth Whitford
Audience: Mostly women 18-30
Quote (for the back): "I always thought I'd know how I'd react if I ever was raped. I was wrong. I've been wrong a lot lately."
Summary (back cover): When twenty-seven-year-old Dana Whitford wakes up with a gut-wrenching feeling, she has little memory of the horrifying events that occurred the night before. Days earlier, Dana was a spirited single mom who had abandoned her hometown to raise her daughter in the city and pursue her dreams. In the short months since Dana’s move to Seattle, she became the adored lover of a charismatic lawyer, started a new business, and finally felt life was going her way. So what happened to cause her to break?

In a gripping and heartbreaking narrative, Dana tells the true story of how her life unraveled from the traumatic events that took place that night and why what seems obvious to everyone else is impossible for Dana to believe. Beneath Quiet Rain is a chilling exploration of memory through trauma, trust in humanity, and a captivating story of strength and survival that appeals to the heart of fathers and mothers, sons and daughters, and men and women alike.
Nice to have
• BACK COVER: I'd like to have a photo on the back. This should depict the happy life of the main character before the sexual assault, and should be with her daughter. Or should be a nature scene that starts at the corner and blends into the rest of the cover. I have attached a possible image or you can use something you like.

```html
<!DOCTYPE html>
<html lang="en">
<head>
<meta charset="utf-8">
<title>Beneath Quiet Rain — Cover</title>
<link href="https://fonts.googleapis.com/css2?family=Bodoni+Moda:wght@400&family=Cormorant+Garamond:wght@500&family=Raleway:wght@400&display=swap" rel="stylesheet">
<style>
  :root {
    --wall-top: #1c2540;
    --wall-mid: #2a3658;
    --wall-low: #34436a;
    --wall-shadow: #243052;
    --linen-deep: #4a3c5c;
    --linen-shadow: #6e5c80;
    --linen-mid: #a895b8;
    --linen-light: #e4dced;
    --title-white: #ffffff;
    --tagline-pink: #f2a9c9;
    --author-white: #f4f2f7;
  }
  * { margin: 0; padding: 0; box-sizing: border-box; }
  html, body { width: 800px; height: 1200px; overflow: hidden; background: var(--wall-top); }
  .cover {
    position: relative;
    width: 800px;
    height: 1200px;
    overflow: hidden;
  }
  .cover-photo {
    position: absolute;
    inset: 0;
    background:
      radial-gradient(ellipse 22% 5% at 38% 68%, rgba(228, 220, 237, 0.85), transparent 75%),
      radial-gradient(ellipse 34% 9% at 70% 72%, rgba(228, 220, 237, 0.7), transparent 75%),
      radial-gradient(ellipse 30% 10% at 25% 95%, rgba(74, 60, 92, 0.9), transparent 75%),
      radial-gradient(ellipse 26% 8% at 88% 93%, rgba(74, 60, 92, 0.75), transparent 75%),
      radial-gradient(ellipse 40% 10% at 55% 82%, rgba(228, 220, 237, 0.75), transparent 75%),
      radial-gradient(ellipse 60% 16% at 50% 86%, var(--linen-mid), transparent 80%),
      radial-gradient(ellipse 70% 40% at 55% 30%, rgba(70, 88, 130, 0.5), transparent 70%),
      linear-gradient(180deg,
        var(--wall-top) 0%,
        var(--wall-mid) 35%,
        var(--wall-low) 52%,
        var(--wall-shadow) 62%,
        var(--linen-shadow) 68%,
        var(--linen-mid) 76%,
        var(--linen-shadow) 90%,
        var(--linen-deep) 100%);
  }
  .tagline {
    position: absolute;
    top: 56px;
    left: 0;
    width: 100%;
    text-align: center;
    font-family: "Cormorant Garamond", serif;
    font-weight: 500;
    font-size: 20px;
    letter-spacing: 1.6px;
    text-transform: uppercase;
    color: var(--tagline-pink);
  }
  .title {
    position: absolute;
    top: 118px;
    left: 0;
    width: 100%;
    text-align: center;
    font-family: "Bodoni Moda", serif;
    font-weight: 400;
    font-size: 132px;
    line-height: 164px;
    color: var(--title-white);
    text-shadow: 0 2px 6px rgba(0, 0, 0, 0.25);
  }
  .title span { display: block; }
  .author {
    position: absolute;
    top: 1054px;
    left: 0;
    width: 100%;
    text-align: center;
    font-family: "Raleway", sans-serif;
    font-weight: 400;
    font-size: 44px;
    letter-spacing: 7px;
    text-transform: uppercase;
    color: var(--author-white);
    text-shadow: 0 1px 4px rgba(0, 0, 0, 0.3);
  }
</style>
</head>
<body>
  <main class="cover">
    <div class="cover-photo" role="img" aria-label="Photograph of an unmade bed with a metal headboard against a dark blue wall, rumpled lavender sheets and a small teddy bear on the pillow"></div>
    <p class="tagline">One Woman's Account of Fear, Guilt &amp; Silence</p>
    <h1 class="title"><span>beneath</span><span>quiet</span><span>rain</span></h1>
    <p class="author">Dana Ruth Whitford</p>
  </main>
</body>
</html>
```